Upmarket Food Product Website (Maple Syrup)

I want an upmarket looking website designed for our maple syrup products which are the best of the best. This website will be to promote the brand only and will not take any orders through it. Therefore the design has to be similar in feel to the examples shown below for both Maple Syrup and Whiskey producers.

https://www.ridgeleafsyrup.com/ (Like this design we will want a similar design)
https://brackenvale.com/us/ (Like the design and colour scheme which goes along with the Maple leaf colours of orange and brown)
http://uk.thehollowmere.com/ (Another good website design)

We have a logo already which we want to keep however if this logo needs to be darker or textured to give it a more upmarket feel then its fine to play around with this can be found in the attachments.

Target Market(s)

US and Canada

Industry/Entity Type

Product

Contact Information for Business Card

President: Neil Parrish
Bramblewick Maple (Quality Maple Syrup)
Tel: (+1) 506-247-8135
Web: www.bramblewickmaple.com
Email: info@bramblewickmaple.com

Coding

Coded - Design and coding required

Number of Pages Required

5+ page

Font styles to use
Sans Serif

Requirements
Must have
• A quality feel, this product is an expensive brand product and as such the website design needs to convey this effectively.
• Must allow for text boxes on each page allowing for 500 words of text to be added at a later stage to each page.
Nice to have
• A similar colour scheme to the logo supplied however the logo may be toned down to darker colours as its a bit bright
Should not have
• Any shopping section or prices for products shown. This site is to build the brand identity and will not offer syrups for sale directly

```html
<!DOCTYPE html>
<html lang="en">
<head>
<meta charset="utf-8">
<title>Bramblewick Maple</title>
<link href="https://fonts.googleapis.com/css2?family=Open+Sans:wght@400;600;700&family=Oswald:wght@500&display=swap" rel="stylesheet">
<style>
:root{
  --green:#1f8a2e;
  --green-dark:#166b22;
  --red:#d7261e;
  --yellow:#f2c014;
  --ink:#333;
  --muted:#666;
  --dark:#2b2523;
  --white:#fff;
}
*{box-sizing:border-box;margin:0;padding:0}
html,body{width:1200px;height:2248px;overflow:hidden}
body{font-family:"Open Sans",Arial,sans-serif;color:var(--ink);background:var(--white);position:relative}
.section{position:absolute;left:0;width:1200px}
.btn{display:inline-block;background:var(--green);color:var(--white);font-size:13px;font-weight:700;padding:8px 16px;border-radius:2px}
.body-text{font-size:12px;line-height:1.5;color:var(--muted)}

/* header */
.header{top:0;height:120px;background:var(--white)}
.logo{position:absolute;left:86px;top:8px;width:160px;height:160px;border-radius:50%;background:var(--white);border:6px solid var(--red);display:flex;align-items:center;justify-content:center;text-align:center;z-index:3;color:var(--red);font-weight:700;font-size:20px;line-height:1.15}
.search{position:absolute;left:490px;top:46px;width:200px;height:28px;border:1px solid #ccc;font-size:12px;color:#999;padding:5px 10px}
.search-btn{position:absolute;left:690px;top:46px;width:28px;height:28px;background:var(--green)}
.social{position:absolute;right:70px;top:44px;display:flex;gap:8px}
.social span{width:30px;height:30px;border-radius:50%;background:#9a9a9a;display:block}
.nav{top:120px;height:40px;background:var(--green)}
.nav ul{list-style:none;display:flex;gap:36px;position:absolute;left:300px;top:10px}
.nav li{color:var(--white);font-weight:600;font-size:15px}

/* hero */
.hero{top:160px;height:520px;background:linear-gradient(180deg,#6b2d10 0%,#b8651c 45%,#e3a043 70%,#f3efe9 100%)}
.feature{position:absolute;top:440px;width:290px;height:290px;border-radius:50%;overflow:hidden;background:var(--white);border:5px solid var(--white);box-shadow:0 4px 12px rgba(0,0,0,.25);z-index:2}
.feature .photo{height:180px}
.feature .label{height:110px;color:var(--white);font-size:12px;text-align:center;padding:22px 40px 0;line-height:1.4}
.feature.red .label{background:var(--red)}
.feature.yellow .label{background:var(--yellow)}
.feature.green .label{background:var(--green)}

/* welcome */
.welcome{top:760px;height:240px;text-align:center}
.title{font-family:"Oswald",Arial,sans-serif;font-size:28px;font-weight:500;color:#222}
.welcome .title{margin-top:10px;padding-bottom:8px;border-bottom:1px solid #ddd;width:1080px;margin-left:60px}
.welcome p{width:1060px;margin:16px auto 0}
.welcome .btn{margin-top:50px}

/* hot offer */
.offer{top:1050px;height:160px;background:linear-gradient(90deg,#3a2a22,#6e5240 50%,#3a2a22);text-align:center;color:var(--white)}
.offer .title{color:var(--white);margin-top:16px}
.offer p{color:#ddd;width:900px;margin:10px auto 0}
.offer .btn{margin-top:12px}

/* story */
.story{top:1240px;height:320px}
.story .photo{position:absolute;left:60px;top:0;width:590px;height:320px;background:linear-gradient(135deg,#6e2a14,#b5532a 50%,#e9d2b4)}
.story .copy{position:absolute;left:670px;top:0;width:470px}
.story h3{font-size:16px;color:var(--green-dark);font-weight:700}
.story p{margin-top:8px}
.story .btn{margin-top:14px}

/* testimonial */
.testimonial{top:1580px;height:150px;background:var(--green)}
.avatar{position:absolute;left:100px;top:18px;width:100px;height:100px;border-radius:50%;background:linear-gradient(#d9b79a,#5a4a40);border:3px solid var(--white)}
.author{position:absolute;left:100px;top:124px;color:var(--white);font-size:11px}
.quote-mark{position:absolute;left:235px;top:10px;color:var(--white);font-size:60px;font-family:Georgia,serif;line-height:1}
.testimonial p{position:absolute;left:270px;top:24px;width:730px;color:#e9f5ea}
.testimonial .btn{position:absolute;left:1020px;top:104px;background:var(--white);color:var(--green);padding:5px 12px;font-size:11px}

/* contact */
.contact{top:1760px;height:320px;background:linear-gradient(180deg,#1e1a18,#3b302a)}
.contact .title{color:var(--white);text-align:center;font-size:24px;margin-top:10px}
.contact .rule{position:absolute;left:180px;top:48px;width:840px;height:1px;background:#777}
.field{position:absolute;left:240px;color:var(--white);font-size:12px}
.input{position:absolute;left:300px;width:180px;height:16px;background:var(--white)}
.message{position:absolute;left:240px;top:152px;width:720px;height:120px;background:rgba(255,255,255,.85);color:#555;font-size:12px;padding:6px 10px}
.contact .btn{position:absolute;left:920px;top:280px;padding:4px 12px;font-size:11px;background:#bbb;color:#222}

/* footer */
.footer{top:2080px;height:168px;background:var(--green);color:var(--white);font-size:12px}
.footer .logo{position:absolute;left:86px;top:8px;width:140px;height:140px;font-size:17px}
.footer .address{position:absolute;left:290px;top:30px;line-height:1.5}
.footer .reach{position:absolute;left:880px;top:30px;line-height:1.8}
.copyright{position:absolute;left:290px;top:120px;font-size:11px;color:#dfeedf}
.icon{display:inline-block;vertical-align:middle;margin-right:6px}
</style>
</head>
<body>

<header class="section header">
  <div class="logo">Bramblewick<br>Maple</div>
  <div class="search">Search</div>
  <div class="search-btn"></div>
  <div class="social"><span></span><span></span><span></span><span></span><span></span></div>
</header>

<nav class="section nav">
  <ul><li>Home</li><li>About Us</li><li>Our Syrups</li><li>Recipes</li><li>Apply To Become A Retailer</li><li>Contact us</li></ul>
</nav>

<section class="section hero" role="img" aria-label="Bottles of amber maple syrup with award medallions"></section>

<div class="feature red" style="left:115px">
  <div class="photo" role="img" aria-label="Glass bowl of maple syrup" style="background:linear-gradient(#f1ede8,#a0521c)"></div>
  <div class="label">Lorem ipsum dolor sit amet consectetur adipiscing elit</div>
</div>
<div class="feature yellow" style="left:455px">
  <div class="photo" role="img" aria-label="Sliced citrus fruit in a bowl" style="background:linear-gradient(#f6e9a8,#d99a2a)"></div>
  <div class="label">Lorem ipsum dolor sit amet consectetur adipiscing elit</div>
</div>
<div class="feature green" style="left:795px">
  <div class="photo" role="img" aria-label="Stack of pancakes topped with syrup" style="background:linear-gradient(#efe6dc,#b8702c)"></div>
  <div class="label">Lorem ipsum dolor sit amet consectetur adipiscing elit</div>
</div>

<section class="section welcome">
  <h2 class="title">Welcome</h2>
  <p class="body-text">Maecenas tincidunt tellus tortor, porta ac pellentesque vel, convallis sed libero. Curabitur ullamcorper magna nec quam aliquet, sed interdum augue viverra. Nulla facilisi. Quisque egestas velit at diam laoreet, a tristique nunc pharetra. Vestibulum ante ipsum primis in faucibus orci luctus et ultrices posuere cubilia. Suspendisse potenti, in hac habitasse platea dictumst nec porta.</p>
  <span class="btn">Learn More</span>
</section>

<section class="section offer" role="img" aria-label="Plated dish on a dark table">
  <h2 class="title">Hot Offer</h2>
  <p class="body-text">Maecenas tincidunt tellus tortor, porta ac pellentesque vel, convallis sed libero. Curabitur ullamcorper magna nec quam aliquet, sed interdum augue viverra. Nulla facilisi, quisque egestas velit at diam laoreet.</p>
  <span class="btn">Learn More</span>
</section>

<section class="section story">
  <div class="photo" role="img" aria-label="Glazed bacon strips on a baking tray"></div>
  <div class="copy">
    <h3>Quite Possibly the Purest Maple Syrup on Earth!</h3>
    <p class="body-text">Quite possibly the purest maple syrup on earth. Ridgeleaf Maple Syrup sets a new standard for organic maple syrup in terms of purity and quality by pairing the best nature has to offer with artisan craftsmanship and breakthrough processing techniques. Ridgeleaf Maple Syrup is painstakingly crafted to deliver unique taste profiles that enhance any recipe, from dessert to dinner. Our trees grow on protected highland estates, and every batch is tested by hand before bottling.</p>
    <p class="body-text">Ridgeleaf Maple Syrup sets a new standard for organic maple syrup in terms of purity and quality by pairing the best nature has to offer with artisan craftsmanship. Each grade is crafted to bring out its own character, from the lightest golden to the darkest robust finish, and every bottle reflects the care of a small family sugarhouse working through the short spring season.</p>
    <span class="btn">Read More</span>
  </div>
</section>

<section class="section testimonial">
  <div class="avatar" role="img" aria-label="Portrait of a customer"></div>
  <div class="author">Owen Hartley</div>
  <div class="quote-mark">&ldquo;</div>
  <p class="body-text">Nothing pancakes to compare. Ridgeleaf Maple Syrup sets a new standard for organic maple syrup in terms of purity and quality by pairing the best nature has to offer with artisan craftsmanship and breakthrough processing techniques. Every bottle is crafted to deliver unique taste profiles that enhance any recipe, from breakfast through to dessert, and my family will not use anything else.</p>
  <span class="btn">Read More</span>
</section>

<section class="section contact">
  <h2 class="title">Email Us</h2>
  <div class="rule"></div>
  <div class="field" style="top:72px">Email</div><div class="input" style="top:72px"></div>
  <div class="field" style="top:98px">Name</div><div class="input" style="top:98px"></div>
  <div class="field" style="top:124px">Subject</div><div class="input" style="top:124px"></div>
  <div class="message">Message</div>
  <span class="btn">Send</span>
</section>

<footer class="section footer">
  <div class="logo">Bramblewick<br>Maple</div>
  <div class="address">
    <svg class="icon" width="12" height="16" viewBox="0 0 12 16"><path d="M6 0a6 6 0 0 0-6 6c0 4.5 6 10 6 10s6-5.5 6-10a6 6 0 0 0-6-6zm0 8.5A2.5 2.5 0 1 1 6 3.5a2.5 2.5 0 0 1 0 5z" fill="#fff"/></svg>Address : Bramblewick Maple<br>
    <span style="margin-left:18px">212 Sugar Bush Lane</span><br>
    <span style="margin-left:18px">Fredericton, New Brunswick</span>
  </div>
  <div class="reach">
    <svg class="icon" width="14" height="14" viewBox="0 0 14 14"><path d="M3 1l2 3-1.5 1.5a8 8 0 0 0 5 5L10 9l3 2-1 2.5C6 14 0 8 0.5 2z" fill="#fff"/></svg>Phone : (+1) 506-247-8135<br>
    <svg class="icon" width="14" height="14" viewBox="0 0 14 14"><circle cx="7" cy="7" r="6" fill="none" stroke="#fff" stroke-width="1.5"/><path d="M1 7h12M7 1c3 3 3 9 0 12M7 1c-3 3-3 9 0 12" fill="none" stroke="#fff"/></svg>www.bramblewickmaple.com<br>
    <svg class="icon" width="14" height="12" viewBox="0 0 14 12"><rect x="0.5" y="0.5" width="13" height="11" fill="none" stroke="#fff"/><path d="M0.5 0.5l6.5 6 6.5-6" fill="none" stroke="#fff"/></svg>Email : info@bramblewickmaple.com
  </div>
  <div class="copyright">Copyright &copy; 2015 Bramblewick Maple</div>
</footer>

</body>
</html>
```